BrookhavenLLC

Real Estate Investment. Buy/Sell house/investment . Trustworthy,Reliable, and friendly

Industry/Entity Type

Real Estate

Contact Information for Business Card

Brookhaven@mailbox-example.com
808-555-0143
Linnea-Joy Patterson

```html
<!DOCTYPE html>
<html lang="en">
<head>
<meta charset="UTF-8">
<title>BrookhavenLLC – Business Card</title>
<link rel="stylesheet" href="https://fonts.googleapis.com/css2?family=Open+Sans:wght@700&family=Raleway:wght@300&display=swap">
<style>
  :root {
    --page-bg: #ededed;
    --card-navy: #0c3f58;
    --ink-white: #ffffff;
  }
  * { margin: 0; padding: 0; box-sizing: border-box; }
  html, body {
    width: 1200px;
    height: 795px;
    overflow: hidden;
    background: var(--page-bg);
  }
  .business-card {
    position: absolute;
    left: 105px;
    top: 112px;
    width: 982px;
    height: 572px;
    background: var(--card-navy);
    color: var(--ink-white);
  }
  .brand {
    position: absolute;
    left: 47px;
    top: 45px;
    display: flex;
    align-items: center;
    gap: 20px;
  }
  .brand-square {
    width: 92px;
    height: 92px;
    background: var(--ink-white);
  }
  .brand-name {
    font-family: "Open Sans", sans-serif;
    font-weight: 700;
    font-size: 48px;
    line-height: 1;
    color: var(--ink-white);
  }
  .services {
    position: absolute;
    left: 0;
    width: 942px;
    text-align: center;
    line-height: 1;
  }
  .services-list {
    top: 249px;
    font-family: "Open Sans", sans-serif;
    font-weight: 700;
    font-size: 31px;
  }
  .services-values {
    top: 288px;
    font-family: "Raleway", sans-serif;
    font-weight: 300;
    font-size: 34px;
  }
  .contact {
    position: absolute;
    right: 48px;
    text-align: right;
    line-height: 1;
    white-space: nowrap;
  }
  .contact-name {
    top: 398px;
    font-family: "Raleway", sans-serif;
    font-weight: 300;
    font-size: 46px;
  }
  .contact-phone,
  .contact-email {
    font-family: "Open Sans", sans-serif;
    font-weight: 700;
    font-size: 32px;
  }
  .contact-phone { top: 454px; }
  .contact-email { top: 495px; }
</style>
</head>
<body>
  <section class="business-card">
    <div class="brand">
      <span class="brand-square" aria-hidden="true"></span>
      <span class="brand-name">BrookhavenLLC</span>
    </div>

    <p class="services services-list">Buy/ Sell house/ Investment</p>
    <p class="services services-values">Trustworthy, Reliable, and Friendly</p>

    <p class="contact contact-name">Joy Patterson</p>
    <p class="contact contact-phone">Linnea. Phone: 808-555-0143</p>
    <p class="contact contact-email">Brookhaven@mailbox-example.com</p>
  </section>
</body>
</html>
```